Wrelby needs a CD cover artwork for the song "Under Quiet Skies"

Hi, I need a CD cover artwork for my new song "Under Quiet Skies". I want to have an image of "Earth" for it. The earth image can be either picturesque or unique artistic. And also, it needs to contain the logo "Wrelby" and "Under Quiet Skies".
jpg. file is necessary.
And I don't like something purchased from the stock image which I need to pay additionally. Original image is preferable.

Target Market(s)

Music

Colors

Designer to choose colors to be used in the design.

Requirements
Must have
• -Earth image
• -The logo "Wrelby" and "Under Quiet Skies"
Nice to have
• -A whole globe image of the earth might be good, rather than a part of the globe or scene of the earth.
• -Something awe-inspiring image might be good.
• -The logo "Wrelby" and "Under Quiet Skies" better fuse to the image nicely rather than oddly standing out from the image.
Should not have
• -the stock image which I need to pay additionally

```html
<!DOCTYPE html>
<html lang="en">
<head>
<meta charset="utf-8">
<title>Wrelby – Under Quiet Skies</title>
<link rel="stylesheet" href="https://fonts.googleapis.com/css2?family=Arimo:wght@700&family=Roboto:wght@100&display=swap">
<style>
  :root {
    --backdrop: #000000;
    --frame: #ffffff;
    --title-red: #d80000;
    --artist-white: #ffffff;
    --art-teal: #1f6a72;
    --art-pink: #b85a8c;
    --art-orange: #d8902c;
    --art-red: #a8242e;
    --art-dark: #141820;
    --globe-blue: #5fa6d8;
    --globe-green: #6fb08a;
    --flare: rgba(190, 255, 255, 0.95);
  }
  html, body {
    margin: 0;
    padding: 0;
    width: 1200px;
    height: 1200px;
    overflow: hidden;
    background: var(--backdrop);
  }
  .cover {
    position: relative;
    width: 1200px;
    height: 1200px;
    background: var(--backdrop);
  }
  .cover-frame {
    position: absolute;
    left: 32px;
    top: 28px;
    width: 1108px;
    height: 1154px;
    border: 3px solid var(--frame);
    box-sizing: border-box;
    overflow: hidden;
  }
  .artwork {
    position: absolute;
    inset: 0;
    background:
      radial-gradient(ellipse 32% 30% at 74% 48%, var(--art-orange) 0%, rgba(216,144,44,0) 100%),
      radial-gradient(ellipse 28% 36% at 34% 58%, var(--art-pink) 0%, rgba(184,90,140,0) 100%),
      radial-gradient(ellipse 30% 30% at 84% 74%, var(--art-red) 0%, rgba(168,36,46,0) 100%),
      radial-gradient(ellipse 40% 30% at 20% 28%, var(--art-teal) 0%, rgba(31,106,114,0) 100%),
      linear-gradient(180deg, var(--art-dark) 0%, #2a3a48 40%, #3a2a40 85%, #1c1c22 100%);
  }
  .earth-globe {
    position: absolute;
    left: 136px;
    top: 402px;
    width: 560px;
    height: 560px;
    border-radius: 50%;
    background:
      radial-gradient(circle at 36% 32%, rgba(255,255,255,0.45) 0%, rgba(255,255,255,0) 28%),
      radial-gradient(circle at 58% 62%, rgba(111,176,138,0.55) 0%, rgba(111,176,138,0) 45%),
      radial-gradient(circle at 50% 50%, rgba(95,166,216,0.65) 0%, rgba(40,90,150,0.55) 62%, rgba(20,40,80,0.35) 100%);
    box-shadow: 0 0 60px rgba(150, 210, 255, 0.25);
  }
  .flares {
    position: absolute;
    inset: 0;
    pointer-events: none;
  }
  .title {
    position: absolute;
    left: 70px;
    width: 1016px;
    top: 72px;
    margin: 0;
    text-align: center;
    white-space: nowrap;
    font-family: "Arimo", Arial, sans-serif;
    font-weight: 700;
    font-size: 116px;
    line-height: 1;
    color: var(--title-red);
  }
  .artist {
    position: absolute;
    left: 68px;
    top: 1064px;
    margin: 0;
    font-family: "Roboto", Helvetica, sans-serif;
    font-weight: 100;
    font-size: 110px;
    line-height: 1;
    color: var(--artist-white);
  }
</style>
</head>
<body>
  <main class="cover">
    <div class="cover-frame">
      <div class="artwork" role="img" aria-label="Street mural of a roaring lion in teal, pink, orange and red tones"></div>
    </div>

    <div class="earth-globe" role="img" aria-label="Translucent Earth globe cradled in an open hand over the mural"></div>

    <svg class="flares" width="1200" height="1200" viewBox="0 0 1200 1200" aria-hidden="true">
      <defs>
        <radialGradient id="glow">
          <stop offset="0" stop-color="#ffffff"/>
          <stop offset="0.25" stop-color="var(--flare)"/>
          <stop offset="1" stop-color="rgba(120,230,240,0)"/>
        </radialGradient>
      </defs>
      <circle cx="86" cy="96" r="34" fill="url(#glow)"/>
      <circle cx="1088" cy="96" r="34" fill="url(#glow)"/>
      <ellipse cx="656" cy="1178" rx="120" ry="10" fill="url(#glow)" opacity="0.8"/>
    </svg>

    <h1 class="title">Under Quiet Skies</h1>
    <p class="artist">Wrelby</p>
  </main>
</body>
</html>
```